Quill Forge Solutions
Bold and Unique
Project: Quill Forge Solutions
Quill Forge Solutions -
Creative Brief
Simple
Gary Holbrook
Owner / IT Consultant
Gary@TheQuillForge.com
www.TheQuillForge.com
Please use either black and white, or black and red if you can... but if you find something that works better, than that works too!! Please be as creative and bold as possible!

```html
<!DOCTYPE html>
<html lang="en">
<head>
<meta charset="UTF-8">
<title>Quill Forge Solutions – Business Card</title>
<link rel="stylesheet" href="https://fonts.googleapis.com/css2?family=Arimo:wght@400;700&display=swap">
<style>
  :root {
    --page-bg: #ffffff;
    --card-black: #000000;
    --card-red: #ed1c24;
    --brand-red: #e0242b;
    --text-white: #ffffff;
  }
  * { margin: 0; padding: 0; box-sizing: border-box; }
  html, body {
    width: 1200px;
    height: 850px;
    overflow: hidden;
    background: var(--page-bg);
    font-family: "Arimo", Arial, sans-serif;
  }
  .canvas {
    position: relative;
    width: 1200px;
    height: 850px;
  }
  .card {
    position: absolute;
    left: 365px;
    top: 41px;
    width: 470px;
    height: 766px;
    background: var(--card-red);
    overflow: hidden;
  }
  .card-top {
    position: absolute;
    left: 0;
    top: 0;
    width: 100%;
    height: 380px;
    background: var(--card-black);
  }
  .brand-mark {
    position: absolute;
    left: 50%;
    top: 60px;
    width: 130px;
    height: 130px;
    margin-left: -65px;
    border-radius: 50%;
    background: var(--brand-red);
  }
  .brand-name {
    position: absolute;
    left: 0;
    top: 195px;
    width: 100%;
    text-align: center;
    color: var(--text-white);
    font-weight: 700;
    font-size: 25px;
    letter-spacing: 2px;
    text-transform: uppercase;
  }
  .tagline {
    position: absolute;
    left: 0;
    top: 290px;
    width: 100%;
    text-align: center;
    color: var(--text-white);
    font-weight: 700;
    font-size: 19px;
  }
  .person {
    position: absolute;
    left: 120px;
    top: 436px;
    color: var(--text-white);
    font-weight: 700;
  }
  .person-name { font-size: 31px; line-height: 36px; }
  .person-role { font-size: 22px; line-height: 30px; }
  .contact-list {
    position: absolute;
    left: 88px;
    top: 592px;
    list-style: none;
    color: var(--text-white);
    font-weight: 700;
    font-size: 21px;
  }
  .contact-item {
    display: flex;
    align-items: center;
    height: 32px;
  }
  .contact-icon {
    width: 20px;
    height: 20px;
    margin-right: 12px;
    fill: var(--text-white);
  }
</style>
</head>
<body>
<div class="canvas">
  <section class="card">
    <div class="card-top">
      <div class="brand-mark"></div>
      <div class="brand-name">Quill Forge Solutions</div>
      <div class="tagline">Strength &amp; Clarity in Every Build</div>
    </div>

    <div class="person">
      <div class="person-name">Gary Holbrook</div>
      <div class="person-role">Owner/IT Consultant</div>
    </div>

    <ul class="contact-list">
      <li class="contact-item">
        <svg class="contact-icon" viewBox="0 0 24 24" aria-hidden="true">
          <path d="M6.6 10.8a15.1 15.1 0 0 0 6.6 6.6l2.2-2.2a1 1 0 0 1 1-.25 11.4 11.4 0 0 0 3.6.57 1 1 0 0 1 1 1V20a1 1 0 0 1-1 1A17 17 0 0 1 3 4a1 1 0 0 1 1-1h3.5a1 1 0 0 1 1 1c0 1.250.2 2.45.57 3.57a1 1 0 0 1-.25 1z"/>
        </svg>
        5550142398
      </li>
      <li class="contact-item">
        <svg class="contact-icon" viewBox="0 0 24 24" aria-hidden="true">
          <path d="M3 5h18a1 1 0 0 1 1 1v12a1 1 0 0 1-1 1H3a1 1 0 0 1-1-1V6a1 1 0 0 1 1-1zm9 7.2L4.5 7.5v1.9L12 14l7.5-4.6V7.5z"/>
        </svg>
        Gary@TheQuillForge.com
      </li>
      <li class="contact-item">
        <svg class="contact-icon" viewBox="0 0 24 24" aria-hidden="true">
          <path d="M12 2a10 10 0 1 0 0 20 10 10 0 0 0 0-20zm6.9 6h-3a15.6 15.6 0 0 0-1.3-3.9A8 8 0 0 1 18.9 8zM12 4c.8 1.1 1.5 2.5 1.9 4h-3.8c.4-1.5 1.1-2.9 1.9-4zM4.3 14a8.2 8.2 0 0 1 0-4h3.4a16 16 0 0 0 0 4zm.8 2h3a15.6 15.6 0 0 0 1.3 3.9A8 8 0 0 1 5.1 16zm3-8h-3a8 8 0 0 1 4.3-3.9A15.6 15.6 0 0 0 8.1 8zM12 20c-.8-1.1-1.5-2.5-1.9-4h3.8c-.4 1.5-1.1 2.9-1.9 4zm2.3-6H9.7a14 14 0 0 1 0-4h4.6a14 14 0 0 1 0 4zm.3 5.9a15.6 15.6 0 0 0 1.3-3.9h3a8 8 0 0 1-4.3 3.9zM16.3 14a16 16 0 0 0 0-4h3.4a8.2 8.2 0 0 1 0 4z"/>
        </svg>
        www.TheQuillForge.com
      </li>
    </ul>
  </section>
</div>
</body>
</html>
```